Health Coaching Brochure for Healthcare Practioners

I am looking to have a tri-fold brochure created marketed towards healthcare practitioners (doctors, nurses, surgeons, etc), to get them to purchase 1-on-1 health coaching from me.
I've provided the text/content (in pdf & pages), my logo, a picture of me, and two color palettes, but please also include lots of white space. I would like to design to be very clean, modern & crisp. Also include additional photos, of doctors, etc taking care of themselves & feeling happy (maybe eating healthy, maybe exercising, feeling good & happy!)
Please also see http://tallbirchwellness.com and http://instagram.com/tallbirchwellness for a feel of my brand.
Thank you!
Target Market(s)
Healthcare Practioners (mainly based in Los Angeles, for now)
Industry/Entity Type
Healthcare
Look and feel
Each slider illustrates characteristics of the customer's brand and the style your logo design should communicate.

```html
<!DOCTYPE html>
<html lang="en">
<head>
<meta charset="utf-8">
<title>Tall Birch Wellness – Tri-fold Brochure</title>
<link href="https://fonts.googleapis.com/css2?family=Dancing+Script:wght@600;700&family=Lato:wght@400;700;900&family=Oswald:wght@500;700&display=swap" rel="stylesheet">
<style>
  :root{
    --bg:#d6d7d9;
    --paper:#ffffff;
    --blue:#3f70ad;
    --blue-deep:#2f5d98;
    --blue-light:#9cbce2;
    --maroon:#8c2232;
    --ink:#2e2e2e;
    --muted:#5a5a5a;
  }
  *{box-sizing:border-box;margin:0;padding:0}
  html,body{width:914px;height:1200px;overflow:hidden;background:var(--bg)}
  body{position:relative;font-family:"Lato",sans-serif;color:var(--ink)}
  .sheet{position:absolute;left:27px;width:860px;height:570px;background:var(--paper);display:flex;box-shadow:0 4px 14px rgba(0,0,0,.18);overflow:hidden}
  .sheet--outside{top:20px}
  .sheet--inside{top:610px}
  .panel{position:relative;width:286.67px;height:100%;overflow:hidden}
  .panel + .panel{border-left:1px solid rgba(0,0,0,.06)}
  .photo{position:absolute;overflow:hidden}
  .script{font-family:"Dancing Script",cursive;font-weight:700;color:var(--maroon)}
  .cond{font-family:"Oswald",sans-serif}

  /* outside / left flap */
  .flap__title{position:absolute;left:28px;font-size:22px}
  .flap__list{position:absolute;left:34px;right:24px;font-size:10.5px;line-height:1.35;list-style:none}
  .flap__list li{position:relative;padding-left:10px}
  .flap__list li::before{content:"";position:absolute;left:0;top:5px;width:4px;height:4px;border-radius:50%;background:var(--maroon)}
  .photo--beach{left:-20px;right:-20px;top:318px;bottom:0;border-radius:55% 55% 0 0/22% 22% 0 0;border-top:5px solid var(--maroon);background:linear-gradient(180deg,#8fb0cf 0%,#4f7ea6 40%,#c9c1b2 70%,#a89f92 100%)}

  /* outside / back panel */
  .back{background:linear-gradient(180deg,var(--blue-light) 0%,#6d98cc 45%,var(--blue) 100%);color:#fff;text-align:center}
  .photo--portrait{left:50%;top:28px;width:130px;height:130px;margin-left:-65px;border-radius:50%;border:4px solid #fff;background:linear-gradient(180deg,#e9d6cc,#7a5a4e)}
  .back__title{position:absolute;top:170px;width:100%;font-size:19px;font-weight:900;color:var(--ink)}
  .back__bio{position:absolute;top:200px;left:26px;right:22px;font-size:7.6px;line-height:1.4;text-align:justify;color:#1f2f45}
  .back__bio p + p{margin-top:6px}
  .back__contact{position:absolute;top:352px;width:100%;font-size:17px;color:var(--ink);letter-spacing:.5px}
  .back__icon{display:block;margin:4px auto 2px}
  .back__phone{position:absolute;top:392px;width:100%;font-size:20px;font-weight:900;color:var(--ink)}
  .back__mail{position:absolute;top:436px;width:100%;font-size:9px;font-weight:700;color:var(--ink)}
  .back__web{position:absolute;top:452px;width:100%;font-size:9px;font-weight:700;color:var(--ink)}
  .back__cta-bg{position:absolute;left:-60px;right:-60px;top:478px;height:200px;border-radius:50%;background:var(--paper)}
  .back__cta{position:absolute;top:498px;width:100%;color:var(--maroon);font-weight:900;text-transform:uppercase}
  .back__cta small{display:block;font-size:8px;color:var(--ink)}
  .back__cta strong{display:block;font-size:12.5px;letter-spacing:.3px}

  /* outside / cover */
  .photo--food{left:0;right:0;top:0;height:300px;background:linear-gradient(135deg,#b9b3a8 0%,#8b7f6e 40%,#c9a86a 70%,#6f6b66 100%)}
  .photo--doctor{left:36px;top:102px;width:224px;height:224px;border-radius:50%;border:5px solid var(--paper);outline:3px solid var(--maroon);outline-offset:-1px;background:linear-gradient(180deg,#f3f5f8,#cfd8e2)}
  .cover__band{position:absolute;left:0;right:0;top:318px;bottom:0;background:var(--paper)}
  .cover__name{position:absolute;top:372px;left:0;right:0;text-align:center;font-size:18px;letter-spacing:.5px;color:var(--ink)}
  .cover__name::before{content:"";display:inline-block;width:8px;height:8px;background:var(--maroon);border-radius:50%;margin-right:8px;vertical-align:middle}
  .cover__tag{position:absolute;top:406px;left:0;right:0;text-align:center;font-size:21px;line-height:1.2}
  .cover__web{position:absolute;top:470px;left:0;right:0;text-align:center;font-size:8px;letter-spacing:1.5px;color:var(--muted)}

  /* inside / programs */
  .photo--tray{left:0;right:0;top:0;height:300px;border-radius:0 0 55% 55%/0 0 20% 20%;border-bottom:5px solid var(--maroon);background:linear-gradient(135deg,#e8e6e3 0%,#c8b08c 45%,#b5473a 60%,#7fa35a 75%,#e3e0dc 100%)}
  .programs{position:absolute;left:0;right:0;top:280px;bottom:0;background:var(--blue);color:#fff;padding:44px 22px 0 26px;z-index:-1}
  .programs__kicker{font-family:"Dancing Script",cursive;font-weight:700;font-size:20px}
  .programs__title{font-size:14px;font-weight:700;margin:4px 0 6px}
  .programs__list{list-style:none;font-size:11px;line-height:1.45}
  .programs__list li::before{content:"•";margin-right:6px}
  .programs__note{font-size:14px;font-weight:700;line-height:1.2;margin-top:10px}
  .programs__access{font-size:14px;font-weight:900;margin-top:12px;letter-spacing:.3px}

  /* inside / course */
  .course{padding:26px 22px 0 28px}
  .course__intro{font-size:11px;line-height:1.35;margin-bottom:10px}
  .course__head{font-family:"Oswald",sans-serif;font-weight:500;font-size:12px;line-height:1.15;color:var(--maroon);text-transform:uppercase;margin-top:10px}
  .course__text{font-size:8.4px;line-height:1.4;margin-top:4px;color:var(--ink)}
  .course__text em{font-style:italic;font-weight:700}
  .course__cta{margin-top:14px;font-family:"Oswald",sans-serif;font-weight:700;font-size:11px;line-height:1.2;text-transform:uppercase;text-align:center}
  .course__cta span{color:var(--blue)}
  .course__today{font-family:"Oswald",sans-serif;font-weight:700;font-size:44px;color:var(--maroon);text-align:center;line-height:1;margin-top:2px}
  .photo--salmon{left:0;right:0;bottom:0;height:138px;background:linear-gradient(90deg,#f5efe6 0%,#d58557 35%,#b4663f 55%,#4f6b31 80%,#f3efe8 100%)}

  /* inside / testimonials */
  .quotes{padding:24px 22px 0 24px}
  .quotes__title{display:flex;align-items:center;gap:8px;justify-content:center;font-family:"Dancing Script",cursive;font-weight:700;font-size:28px;color:var(--blue)}
  .quotes__title::before,.quotes__title::after{content:"";width:26px;height:1.5px;background:var(--blue)}
  .quote{margin-top:10px}
  .quote__lead{font-family:"Oswald",sans-serif;font-weight:500;font-size:11px;line-height:1.2;text-transform:uppercase;color:var(--maroon)}
  .quote__text{font-size:8px;line-height:1.4;margin-top:6px}
  .quote__by{font-family:"Oswald",sans-serif;font-weight:700;font-size:10px;color:var(--maroon);text-align:right;margin-top:4px}
  .photo--clients{left:0;right:-30px;top:388px;bottom:-10px;border-radius:70% 0 0 0/60% 0 0 0;border-top:5px solid var(--blue);border-left:5px solid var(--blue);background:linear-gradient(135deg,#c44a3a 0%,#e7d3c6 40%,#8d8f94 70%,#3c3c3f 100%)}
</style>
</head>
<body>

<section class="sheet sheet--outside" aria-label="Brochure outside">
  <div class="panel flap">
    <h2 class="flap__title script" style="top:30px">Are You Feeling...</h2>
    <ul class="flap__list" style="top:66px">
      <li>Overwhelmed?</li>
      <li>Exhausted?</li>
      <li>Struggling with food and feeling guilty about it?</li>
      <li>Like you know what you SHOULD do but aren't doing it?</li>
    </ul>
    <h2 class="flap__title script" style="top:172px">How Would It Feel To ...</h2>
    <ul class="flap__list" style="top:208px">
      <li>Wake up feeling light and energized?</li>
      <li>Finally get a handle on food and your cravings?</li>
      <li>Reach all of your health goals and life goals?</li>
    </ul>
    <div class="photo photo--beach" role="img" aria-label="Photo of a woman jumping joyfully on a beach by the sea"></div>
  </div>

  <div class="panel back">
    <div class="photo photo--portrait" role="img" aria-label="Portrait photo of the health coach"></div>
    <h2 class="back__title">About me</h2>
    <div class="back__bio">
      <p>Dana Whitlow is a personal trainer, fitness nutritionist, and holistic health coach based in Los Angeles, California. Dana helps clients improve their health, develop sustainable habits, and achieve their goals to be their best, most vibrant selves.</p>
      <p>Dana sought fitness in 2005 to overcome her lifelong battle of depression, anxiety, and an extra 30 pounds. After completely transforming her body and her mind, she realized that transformation spilling over to other areas of her life – career, relationships and self-worth. She began to help other people transform their lives, as well.</p>
    </div>
    <div class="back__contact">CONTACT
      <svg class="back__icon" width="12" height="12" viewBox="0 0 24 24" aria-hidden="true"><path fill="#fff" d="M6.6 10.8a15.1 15.1 0 0 0 6.6 6.6l2.2-2.2a1 1 0 0 1 1-.25 11.4 11.4 0 0 0 3.6.6 1 1 0 0 1 1 1V20a1 1 0 0 1-1 1A17 17 0 0 1 3 4a1 1 0 0 1 1-1h3.5a1 1 0 0 1 1 1c0 1.25.2 2.45.6 3.6a1 1 0 0 1-.25 1z"/></svg>
    </div>
    <div class="back__phone">555-014-2290</div>
    <div class="back__mail">dana@tallbirchwellness.com</div>
    <div class="back__web">www.tallbirchwellness.com</div>
    <div class="back__cta-bg"></div>
    <div class="back__cta"><small>Call for a</small><strong>Free 15 Minute Consultation</strong></div>
  </div>

  <div class="panel cover">
    <div class="photo photo--food" role="img" aria-label="Collage of healthy baked snacks and a green smoothie"></div>
    <div class="cover__band"></div>
    <div class="photo photo--doctor" role="img" aria-label="Photo of a smiling doctor in a white coat with a stethoscope"></div>
    <div class="cover__name">tall birch wellness</div>
    <div class="cover__tag script">1-on-1 Health Coaching For<br>Healthcare Practitioners</div>
    <div class="cover__web">www.tallbirchwellness.com</div>
  </div>
</section>

<section class="sheet sheet--inside" aria-label="Brochure inside">
  <div class="panel" style="isolation:isolate">
    <div class="photo photo--tray" role="img" aria-label="Breakfast tray with salad, vegetables and toast on a bed"></div>
    <div class="programs">
      <div class="programs__kicker">Get Healthy. Feel Energized. Thrive!</div>
      <div class="programs__title">Programs &amp; Packages</div>
      <ul class="programs__list">
        <li>1-on-1 Health Coaching (virtual or in-person)</li>
        <li>Group Health Coaching</li>
        <li>Specialized (gluten-free, dairy-free, etc) Meal Plans</li>
        <li>Public Speaking Education</li>
        <li>Nutrition &amp; Supplementation Counseling</li>
        <li>Wedding Preparation</li>
      </ul>
      <div class="programs__note">Integrative Nutrition &amp; Health Coaching available as well.</div>
      <div class="programs__access">+24-HOUR ACCESS TO TRAINER</div>
    </div>
  </div>

  <div class="panel course">
    <p class="course__intro">This 4-week virtual coaching program includes:</p>
    <h3 class="course__head">Health History &amp; Nutrition/Fitness Assessment:</h3>
    <p class="course__text">Prior to our first session together, you will receive and complete an individual health history form, where I can assess your current lifestyle habits, your nutrition &amp; fitness goals, and dietary and health needs.</p>
    <h3 class="course__head">Nutrition Guidelines &amp; Real Food Meal Ideas:</h3>
    <p class="course__text">After completing the health history assessment, you will receive your 4-week nutrition and gut-healing plan before our first virtual coaching session.</p>
    <h3 class="course__head">4 60-Minute Virtual Coaching Sessions:</h3>
    <p class="course__text">4 60-minute coaching sessions held via webinar.<br><em>These sessions will be recorded and sent to all group members, in the case you can't make one.</em></p>
    <div class="course__cta">Ready to make real change?<br>Schedule your <span>15 minute</span> consultation</div>
    <div class="course__today">TODAY!</div>
    <div class="photo photo--salmon" role="img" aria-label="Plate of baked salmon with broccolini held in a hand"></div>
  </div>

  <div class="panel quotes">
    <h2 class="quotes__title">Testimonials</h2>
    <div class="quote">
      <p class="quote__lead">Dana is the perfect balance of tough and caring. She has this way of making me feel like I can push myself without being too stern.</p>
      <p class="quote__text">I love how every session she mixes up the exercises so that they are varied, and never get boring. She is super professional, motivating, knowledgeable and a pleasure to be around. I have been working with her 3X/week for just over a month and I have lost inches off my waist and lost eight pounds. Prior to working with Dana I was super sedentary and since having a baby last year, I just haven't felt good in my body. Dana has made me feel motivated and strong, and after every session I feel confident that I can reach my goals and feel healthy and active again.</p>
      <p class="quote__by">- Rosa Delgado</p>
    </div>
    <div class="quote">
      <p class="quote__lead">I am so happy with the results!</p>
      <p class="quote__text">The fogginess is gone (as are my sugar cravings), I've found new ways to add healthy foods into my diet and (bonus) I lost five pounds the first week!</p>
      <p class="quote__by">- Nina K</p>
    </div>
    <div class="photo photo--clients" role="img" aria-label="Photos of happy clients training in a gym"></div>
  </div>
</section>

</body>
</html>
```